Harbor LunaVital & Equipments

I need to create full stationery design for the company; Business Card, Envelop, Letterheads, Calendar and email template.

Our company is specialized in the import and export of nutritional, pharmaceutical and cosmetics in addition to medical equipments.

These is no limitation on how to use colors within the design.

Target Market(s)

Global

Industry/Entity Type

Healthcare

Other font styles liked:
• a font close to logo. Letterhead body text to be different than the address text

Requirements
Nice to have
• We will have multiple locations so it is good to keep space for future addresses.
• Stationary requirements:
• Letterhead: A4
• Envelopes: 3 regular sizes : large, medium and small (i do not know the sizes)
• Colors: extracted from the logo

```html
<!DOCTYPE html>
<html lang="en">
<head>
<meta charset="utf-8">
<title>Harbor LunaVital &amp; Equipments — Stationery</title>
<link rel="stylesheet" href="https://fonts.googleapis.com/css2?family=Carlito:wght@400;700&family=Poppins:wght@400;600;700&display=swap">
<style>
  :root {
    --navy: #1c1a55;
    --blue: #27a9e1;
    --orange: #fbb12f;
    --green: #25a24a;
    --paper: #ffffff;
    --backdrop: #a3a3a3;
    --ink: #1a1a1a;
    --muted: #3a3a4a;
  }
  * { box-sizing: border-box; margin: 0; padding: 0; }
  html, body { width: 1200px; height: 1000px; overflow: hidden; }
  body { background: var(--backdrop); position: relative; font-family: "Carlito", sans-serif; color: var(--ink); }

  .brand-bar { position: absolute; left: 0; right: 0; display: flex; }
  .brand-bar span { flex: 1; }
  .brand-bar .navy { background: var(--navy); }
  .brand-bar .blue { background: var(--blue); }
  .brand-bar .orange { background: var(--orange); }
  .brand-bar .green { background: var(--green); }

  /* Letterhead */
  .letterhead { position: absolute; left: 70px; top: 125px; width: 507px; height: 716px; background: var(--paper); }
  .letterhead .bar-top { top: 0; height: 8px; }
  .letterhead .bar-bottom { bottom: 0; height: 15px; }
  .letterhead .wordmark { position: absolute; left: 0; right: 0; top: 180px; }
  .wordmark-centered { position: absolute; top: 40px; left: 0; right: 0; display: flex; flex-direction: column; align-items: center; gap: 6px; }
  .brand-square { width: 30px; height: 30px; background: var(--navy); border-radius: 4px; }
  .brand-name { font-family: "Poppins", sans-serif; font-weight: 700; color: var(--blue); line-height: 1.05; text-align: center; }
  .letterhead .brand-name { font-size: 17px; }
  .letter-body { position: absolute; left: 48px; top: 130px; width: 410px; font-size: 9.3px; line-height: 17.3px; }
  .letter-body h2 { font-size: 10px; font-weight: 700; margin-bottom: 16px; }
  .letter-body p { margin-bottom: 17px; }
  .letter-body .closing { font-weight: 700; margin-bottom: 10px; }
  .signature { width: 130px; height: 40px; background: linear-gradient(90deg, #ededed, #dcdcdc); border-radius: 3px; margin-bottom: 4px; }
  .letter-footer { position: absolute; left: 58px; right: 40px; top: 684px; display: flex; align-items: center; gap: 14px; font-family: "Poppins", sans-serif; font-size: 6.3px; color: var(--muted); }
  .letter-footer .item { display: flex; align-items: center; gap: 4px; }
  .letter-footer svg { width: 8px; height: 8px; }
  .letter-footer .address { border-left: 1px solid var(--navy); padding-left: 7px; color: var(--navy); }

  /* Envelope front */
  .envelope-front { position: absolute; left: 597px; top: 185px; width: 569px; height: 267px; background: var(--paper); }
  .envelope-front .bar-bottom { bottom: 0; height: 17px; }
  .envelope-front .wordmark { position: absolute; left: 23px; top: 20px; display: flex; align-items: center; gap: 7px; }
  .envelope-front .brand-square { width: 22px; height: 22px; border-radius: 3px; }
  .envelope-front .brand-name { font-size: 12px; text-align: left; }
  .sender-address { position: absolute; left: 23px; top: 74px; font-family: "Poppins", sans-serif; font-size: 6.6px; line-height: 9px; color: var(--muted); }

  /* Envelope back */
  .envelope-back { position: absolute; left: 598px; top: 498px; width: 568px; height: 267px; background: var(--paper); }
  .envelope-back .flap { position: absolute; left: 0; top: 0; width: 568px; height: 66px; }
  .envelope-back .flap-mark { position: absolute; left: 0; right: 0; top: 20px; text-align: center; font-family: "Poppins", sans-serif; font-weight: 700; font-size: 11px; color: var(--paper); }
</style>
</head>
<body>

  <section class="letterhead" aria-label="Letterhead">
    <div class="brand-bar bar-top"><span class="navy"></span><span class="blue"></span><span class="orange"></span><span class="green"></span></div>

    <div class="wordmark-centered">
      <div class="brand-square"></div>
      <div class="brand-name">Harbor LunaVital<br>&amp; Equipments</div>
    </div>

    <div class="letter-body">
      <h2>Lorem Ipsum is simply</h2>
      <p>dummy text of the printing and typesetting industry. Lorem Ipsum has been the industry's standard dummy text ever since the 1500s, when an unknown printer took a galley of type and scrambled it to make a type specimen book. It has survived not only five centuries, but also the leap into electronic typesetting, remaining essentially unchanged. It was popularised in the 1960s with the release of Typeset sheets containing Lorem Ipsum passages, and more recently with desktop publishing software like PageForge including versions of Lorem Ipsum.</p>
      <p>It is a long established fact that a reader will be distracted by the readable content of a page when looking at its layout. The point of using Lorem Ipsum is that it has a more-or-less normal distribution of letters, as opposed to using 'Content here, content here', making it look like readable English. Many desktop publishing packages and web page editors now use Lorem Ipsum as their default model text, and a search for 'lorem ipsum' will uncover many web sites still in their infancy. Various versions have evolved over the years, sometimes by accident, sometimes on purpose (injected humour and the like).</p>
      <p>Contrary to popular belief, Lorem Ipsum is not simply random text. It has roots in a piece of classical Latin literature from 45 BC, making it over 2000 years old. Daniel Ostervelt, a Latin professor at Westbrook College in Vermont, looked up one of the more obscure Latin words, consectetur, from a Lorem Ipsum passage,</p>
      <p class="closing">Lorem Ipsum</p>
      <div class="signature" role="img" aria-label="Handwritten signature"></div>
      <div>Lorem Ipsum is a dummy</div>
    </div>

    <footer class="letter-footer">
      <span class="item">
        <svg viewBox="0 0 10 10"><circle cx="5" cy="5" r="5" fill="var(--navy)"/><path d="M3 2.6l1 .1.4 1.2-.6.5a4 4 0 0 0 1.8 1.8l.5-.6 1.2.4.1 1c-2.6.4-4.8-1.8-4.4-4.4z" fill="#fff"/></svg>
        000-417-2630
      </span>
      <span class="item">
        <svg viewBox="0 0 10 10"><circle cx="5" cy="5" r="5" fill="var(--navy)"/><rect x="3.3" y="2.2" width="3.4" height="5.6" rx=".6" fill="#fff"/></svg>
        000-594-3071
      </span>
      <span class="item">
        <svg viewBox="0 0 10 10"><circle cx="5" cy="5" r="5" fill="var(--navy)"/><circle cx="5" cy="5" r="2.5" fill="none" stroke="#fff" stroke-width=".8"/></svg>
        www.harborlunavital.com
      </span>
      <span class="address">4180 Marrowby Terrace City Name, LA 60214</span>
    </footer>

    <div class="brand-bar bar-bottom"><span class="navy"></span><span class="blue"></span><span class="orange"></span><span class="green"></span></div>
  </section>

  <section class="envelope-front" aria-label="Envelope front">
    <div class="wordmark">
      <div class="brand-square"></div>
      <div class="brand-name">Harbor LunaVital<br>&amp; Equipments</div>
    </div>
    <address class="sender-address" style="font-style:normal">8 Calder House<br>Wrenfield Business Village, City Name</address>
    <div class="brand-bar bar-bottom"><span class="navy"></span><span class="blue"></span><span class="orange"></span><span class="green"></span></div>
  </section>

  <section class="envelope-back" aria-label="Envelope back">
    <svg class="flap" viewBox="0 0 568 66" aria-hidden="true">
      <path d="M0 0 H568 C556 18 548 58 528 64 H40 C20 58 12 18 0 0 Z" fill="var(--navy)"/>
    </svg>
    <div class="flap-mark">Harbor LunaVital</div>
  </section>

</body>
</html>
```